Update the A4 Specials Page for Restaurant/Cafe

Provide a MINIMALIST attractive Specials page we can print weekly for our food and drink specials to give to our guests. Final design is to be provided in WORD Document so it can be easily edited by Manager. Should be black text and MINIMALIST to minimise ink usage as we print hundreds a week. We have UPLOADED the existing page as a template for you to update. Maybe logo can stay, see what you think. Or delete it and do something else. Keep it simple. Choose a good FONT. Could be a little playful with a cocktail ICON or something. Our existing menus can be seen at www.tallpinebistro.com.au and they are using font Alegreya. Please note we are unable to provide any feedback to designers, however we really do appreciate your time if you are submitting a design. Thank you for your participation.

```html
<!DOCTYPE html>
<html lang="en">
<head>
<meta charset="utf-8">
<title>Tall Pine Bistro – Weekly Specials</title>
<link href="https://fonts.googleapis.com/css2?family=Poppins:wght@400;500;600&display=swap" rel="stylesheet">
<style>
  :root {
    --backdrop: #e6e7e8;
    --paper: #ffffff;
    --ink: #111111;
    --ink-soft: #444444;
    --shadow: rgba(0, 0, 0, 0.28);
  }
  * { margin: 0; padding: 0; box-sizing: border-box; }
  html, body {
    width: 676px; height: 1200px; overflow: hidden;
    background: var(--backdrop);
    font-family: "Poppins", sans-serif;
    color: var(--ink);
  }
  .specials-sheet {
    position: absolute; left: 40px; top: 178px;
    width: 596px; height: 842px;
    background: var(--paper);
    box-shadow: 3px 4px 6px var(--shadow);
  }
  .sheet-frame {
    position: absolute; left: 22px; top: 22px; right: 22px; bottom: 22px;
    border: 1px solid var(--ink);
  }
  .brand-gap {
    position: absolute; left: 245px; top: 15px; width: 106px; height: 14px;
    background: var(--paper);
  }
  .brand-block {
    position: absolute; left: 253px; top: 0; width: 89px; height: 100px;
    background: var(--ink);
    display: flex; flex-direction: column; align-items: center; justify-content: center;
    color: var(--paper);
    font-weight: 600; font-size: 11px; line-height: 13px; letter-spacing: 0.5px;
    text-align: center;
  }
  .line {
    position: absolute; left: 0; width: 100%;
    text-align: center; height: 20px; line-height: 20px; white-space: nowrap;
  }
  .section-title { font-weight: 600; font-size: 19px; letter-spacing: 3px; }
  .item-name { font-weight: 400; font-size: 17px; letter-spacing: 2.2px; }
  .item-name.muted { color: var(--ink-soft); }
  .item-detail { font-size: 11px; }
  .price { font-weight: 600; font-size: 17px; }
  .closing-rule {
    position: absolute; left: 235px; top: 774px; width: 124px; height: 3px;
    background: var(--ink);
  }
</style>
</head>
<body>
  <main class="specials-sheet">
    <div class="sheet-frame"></div>
    <div class="brand-gap"></div>
    <div class="brand-block"><span>TALL PINE</span><span>BISTRO</span></div>

    <h1 class="line section-title" style="top:150px">WEEKLY SPECIALS</h1>
    <h2 class="line item-name" style="top:189px">CHICKEN FILO</h2>
    <p class="line item-detail" style="top:214px">Creamy Chicken with Pinenuts. wrapped in Filo Pastry.</p>
    <p class="line item-detail" style="top:233px">Served with Side Salad &amp; Zulu Sauce</p>
    <p class="line price" style="top:261px">$24</p>

    <h2 class="line item-name" style="top:298px">MINESTRONE SOUP</h2>
    <p class="line item-detail" style="top:323px">Served with Garlic Bread</p>
    <p class="line price" style="top:351px">$8</p>

    <h1 class="line section-title" style="top:408px">COCKTAIL SPECIAL</h1>
    <h2 class="line item-name muted" style="top:447px">PASSIONISTA</h2>
    <p class="line item-detail" style="top:473px">Vodka, Passionfruit Pulp, Mango Puree</p>
    <p class="line item-detail" style="top:493px">Top up with Ginger &amp; Lemon Kombucha</p>
    <p class="line price" style="top:521px">$17</p>

    <h1 class="line section-title" style="top:578px">CRAFT BEER SPECIAL</h1>
    <h2 class="line item-name muted" style="top:617px">CROOKED HERON</h2>
    <p class="line item-detail" style="top:642px">SUN DRIFT</p>
    <p class="line item-detail" style="top:661px">Tropical Pale Ale</p>
    <p class="line item-detail" style="top:680px">4.8% Alc.</p>
    <p class="line price" style="top:707px">$10</p>

    <div class="closing-rule"></div>
  </main>
</body>
</html>
```